New Business Card Design for Manufacturing

We are an engineering/manufacturing company that offers Advanced machining/assembly/engineering services, as well as innovative products for the heavy duty engine cooling markets.

We are looking to get a new business card designed that is clean and modern looking, but still fits the wide range of technical/skilled work we do.

- We hope to use this design as the base for other design work in new Presentations, web, and print work.

Industry/Entity Type

Engineering

Contact Information for Business Card

Our preferred color of blue is (RGB) 22/71/159 but can vary slightly from that color. Our content will be our Logo and full company name (Fabricated Tooling Works, Inc.), company address, name, job title, phone number with extension, cell number, fax number, website, and email address on the cards.
We'd like the full company name next to the logo, but we are open to other interpretations of that layout.
Preferably, we would like the back side to be clean with just our logo, and the front to contain all of the contact information.

Colors
2f74b4
0355a3
85abd2

Requirements
Must have
• - Logo, company name, needed content - We are open to interpretation beyond that.
• - Standard size business card.
• - Horizontal orientation.
• - Enough space for lengthy names / job titles (for example, a job title could read "Directory of Human Resources" or "V.P. of Governmental Affairs"). We need this to look clean, whether the title be short (CEO) or long (as described above).

```html
<!DOCTYPE html>
<html lang="en">
<head>
<meta charset="utf-8">
<title>Fabricated Tooling Works – Business Card</title>
<link href="https://fonts.googleapis.com/css2?family=Open+Sans:wght@400;600;700&display=swap" rel="stylesheet">
<style>
  :root {
    --brand-blue: #0b4a97;
    --brand-blue-deep: #0a4288;
    --ink-gray: #5f6368;
    --rule-gray: #8a8d91;
    --card-white: #f4f4f4;
    --backdrop: #1b1c1e;
  }
  * { box-sizing: border-box; margin: 0; padding: 0; }
  html, body {
    width: 1200px; height: 900px; overflow: hidden;
    background: var(--backdrop);
    font-family: "Open Sans", Arial, sans-serif;
  }
  .stage {
    width: 1200px; height: 900px;
    display: flex; flex-direction: column; align-items: center; justify-content: center; gap: 30px;
  }
  .card {
    position: relative; width: 700px; height: 400px; overflow: hidden;
    box-shadow: 0 10px 30px rgba(0,0,0,.5);
  }
  /* Back side */
  .card-back {
    background: linear-gradient(135deg, var(--brand-blue) 0%, var(--brand-blue-deep) 100%);
    display: flex; align-items: center; justify-content: center;
  }
  .back-wordmark {
    display: flex; align-items: center; gap: 12px;
    color: #ffffff; font-weight: 700; font-size: 26px; letter-spacing: .3px;
  }
  .wordmark-square { width: 16px; height: 16px; background: #ffffff; }
  /* Front side */
  .card-front { background: linear-gradient(160deg, #e9e9e9 0%, var(--card-white) 45%, #fbfbfb 100%); }
  .front-wordmark {
    position: absolute; left: 40px; top: 120px; width: 250px;
    display: flex; align-items: flex-start; gap: 10px;
    color: var(--brand-blue); font-weight: 700; font-size: 22px; line-height: 1.25;
  }
  .front-wordmark .wordmark-square { background: var(--brand-blue); margin-top: 6px; flex: none; }
  .divider {
    position: absolute; left: 318px; top: 70px; width: 2px; height: 200px;
    background: var(--rule-gray);
  }
  .contact { position: absolute; left: 348px; top: 62px; color: var(--ink-gray); }
  .contact-name { color: var(--brand-blue); font-weight: 700; font-size: 24px; line-height: 1.2; }
  .contact-title { font-size: 16px; margin-bottom: 12px; }
  .contact-address { font-size: 16px; line-height: 1.4; margin-bottom: 10px; }
  .contact-line { display: flex; align-items: center; gap: 10px; font-size: 15px; line-height: 1.45; }
  .contact-line svg { width: 15px; height: 15px; flex: none; }
  .contact-label { color: var(--brand-blue); font-weight: 700; font-size: 13px; width: 15px; flex: none; text-align: center; }
  .wave { position: absolute; left: 0; bottom: 0; width: 700px; height: 400px; }
  .website {
    position: absolute; left: 430px; top: 360px;
    color: #ffffff; font-size: 17px; letter-spacing: 2px; white-space: nowrap;
  }
  .website strong { font-weight: 700; }
</style>
</head>
<body>
<main class="stage">
  <section class="card card-back" aria-label="Card back">
    <div class="back-wordmark"><span class="wordmark-square"></span>Fabricated Tooling Works, Inc.</div>
  </section>

  <section class="card card-front" aria-label="Card front">
    <svg class="wave" viewBox="0 0 700 400" aria-hidden="true">
      <defs>
        <linearGradient id="sheen" x1="0" y1="0" x2="1" y2="0">
          <stop offset="0" stop-color="#ffffff" stop-opacity="0"/>
          <stop offset="0.7" stop-color="#ffffff" stop-opacity="0.85"/>
          <stop offset="1" stop-color="#ffffff" stop-opacity="0"/>
        </linearGradient>
      </defs>
      <path d="M0,292 C140,330 290,344 420,341 C560,338 650,348 700,352 L700,400 L0,400 Z" fill="var(--brand-blue)"/>
      <path d="M60,312 C160,334 260,342 340,340" fill="none" stroke="url(#sheen)" stroke-width="6"/>
    </svg>

    <div class="front-wordmark"><span class="wordmark-square"></span>Fabricated Tooling Works, Inc.</div>
    <div class="divider"></div>

    <div class="contact">
      <p class="contact-name">Daniel Reyes</p>
      <p class="contact-title">V.P. of Governmental Affairs</p>
      <p class="contact-address">214 Foundry Lane, Suite 3<br>Millbrook, CA 95021</p>
      <p class="contact-line">
        <svg viewBox="0 0 24 24"><path fill="var(--brand-blue)" d="M6.6 10.8a15.1 15.1 0 0 0 6.6 6.6l2.2-2.2a1 1 0 0 1 1-.25 11.4 11.4 0 0 0 3.6.57 1 1 0 0 1 1 1V20a1 1 0 0 1-1 1A17 17 0 0 1 3 4a1 1 0 0 1 1-1h3.5a1 1 0 0 1 1 1c0 1.25.2 2.45.57 3.57a1 1 0 0 1-.25 1z"/></svg>
        +1 555 014 2299 ext. 204
      </p>
      <p class="contact-line"><span class="contact-label">C</span>+1 555 014 7731</p>
      <p class="contact-line"><span class="contact-label">F</span>+1 555 014 2300</p>
      <p class="contact-line">
        <svg viewBox="0 0 24 24"><path fill="var(--brand-blue)" d="M3 5h18a1 1 0 0 1 1 1v12a1 1 0 0 1-1 1H3a1 1 0 0 1-1-1V6a1 1 0 0 1 1-1zm1 2.2V17h16V7.2l-8 5.3z"/></svg>
        info@fabtoolworks.com
      </p>
    </div>

    <p class="website">www.<strong>fabtoolworks</strong>.com</p>
  </section>
</main>
</body>
</html>
```